E-commerce portal dedicated for selling books

We are looking for a design of a professional and official e-commerce web-site for a new company that is specialized in selling books (both books formats, printed and electronic), we’ll deal also with used-books where we plan to buy used books and re-sell them to other clients, or let the clients can sell their used-books directly to another client,
Web site must be very clear for users who like to brows the site contents or to buy a book, we will make the books available in discounted prices.
Customer should be able to perform the following actions in the site:
Search the book he/she is looking for easily
Get a brief description and details about the author, publisher, book content, browse the book’s content, browse first 20 pages ,
View similar or related books and a list of books that other users who bought this books also bought
Read and write reviews
Sign-up in the site
Complete the purchase process
Users can also sell or buy used-books from the site.
Look and feel:
The site’s look and feel is preferred to be clean, simple and balanced
Web site design is preferred to be simple with no strong or dark colors
User should feel comfort when looking at the home page because the design simplicity and comfortable colors
I liked the following sites’ look and feel:
http://www.qirtas.ae/
http://www.velmora.com/
http://www.tulvinghart.com/
Please be sure to include all common elements that are used in the e-commerce web sites like Search, online form(s), shopping cart / ordering, user log in/member, printer-friendly function, subscription to newsletter.....

```html
<!DOCTYPE html>
<html lang="en">
<head>
<meta charset="utf-8">
<title>Online BookStore</title>
<link rel="stylesheet" href="https://fonts.googleapis.com/css2?family=Open+Sans:wght@400;600;700&display=swap">
<style>
:root{
  --blue:#1d8fdc;
  --blue-dark:#1572b6;
  --pink:#e3197b;
  --text:#222;
  --muted:#555;
  --line:#d6d6d6;
  --band:#f2f2f2;
  --star:#f39a12;
  --star-off:#555;
}
*{box-sizing:border-box;margin:0;padding:0}
html,body{width:1200px;height:2329px;overflow:hidden}
body{font-family:"Open Sans",Arial,sans-serif;color:var(--text);background:#fff;position:relative;font-size:13px}
.wrap{position:absolute;left:127px;width:946px}

/* header */
.brand{top:30px;display:flex;align-items:center;gap:12px}
.brand-mark{width:52px;height:52px;background:var(--blue);border-radius:4px}
.brand-name{font-size:26px;font-weight:700;color:var(--blue);line-height:1}
.social{position:absolute;right:0;top:8px;display:flex;gap:10px;font-size:12px;font-weight:600;color:var(--blue);white-space:nowrap}
.toolbar{top:116px;height:40px;display:flex;gap:8px}
.search{flex:0 0 708px;display:flex;border:3px solid var(--blue);border-radius:4px;background:var(--blue);overflow:hidden}
.search-input{flex:1;background:#fff;color:#aaa;padding:0 12px;line-height:34px;font-size:13px}
.search-by{color:#fff;width:36px;text-align:center;line-height:34px;font-size:13px;background:var(--blue-dark)}
.search-field{width:172px;background:#fff;line-height:34px;padding:0 12px;color:#333;display:flex;justify-content:space-between}
.search-btn{width:108px;color:#fff;font-size:17px;font-weight:600;text-align:center;line-height:34px;white-space:nowrap}
.account{display:flex;flex:1}
.account span{flex:1;border:1px solid #bbb;background:linear-gradient(#fafafa,#dedede);line-height:38px;text-align:center;font-size:12px;color:#333;white-space:nowrap}
.account span+span{border-left:0}
.nav{position:absolute;top:166px;left:0;width:1200px;height:47px;background:linear-gradient(#fcfcfc,#e4e4e4);border-top:1px solid var(--line);border-bottom:1px solid #c8c8c8}
.nav ul{position:absolute;left:127px;width:946px;display:flex;list-style:none;height:100%}
.nav li{flex:0 0 auto;white-space:nowrap;padding:0 12px;line-height:45px;font-size:12.5px;border-right:1px solid #c9c9c9;color:#333}
.nav li:first-child{padding-left:4px}
.nav li:last-child{border-right:0;padding-right:0}

/* hero */
.hero-band{position:absolute;top:213px;left:0;width:1200px;height:385px;background:#f2f2f2}
.hero{top:244px;height:307px;border:3px solid #c7d4de;background:linear-gradient(90deg,#6e9ccb,#a9c7e2 55%,#cfe0ee);box-shadow:0 10px 12px -6px rgba(0,0,0,.35)}
.hero-copy{position:absolute;left:50px;top:50px;width:440px;text-align:center}
.hero-copy h1{font-size:29px;font-weight:700;color:#1f1f1f;letter-spacing:.5px;white-space:nowrap}
.hero-copy h2{font-size:23px;font-weight:400;color:#222;margin-top:4px}
.hero-copy .by{font-size:13px;margin-top:2px}
.hero-copy p{font-size:14px;color:#222;margin-top:6px;line-height:1.35}
.hero-buy{position:absolute;left:60px;top:198px;display:flex;align-items:center;gap:44px}
.price{font-size:19px;font-weight:700;color:#1565c0}
.btn-light{width:115px;height:28px;border:1px solid #aaa;background:linear-gradient(#fff,#ddd);color:var(--blue-dark);font-weight:700;font-size:14px;text-align:center;line-height:26px;border-radius:2px}
.hero-cover{position:absolute;left:511px;top:15px;width:374px;height:274px;background:linear-gradient(90deg,#2a2c33,#4a4d57 55%,#6b6e78)}
.dots{position:absolute;left:30px;bottom:14px;display:flex;gap:5px}
.dots i{width:12px;height:12px;background:#fff;display:block}
.dots i:first-child{background:var(--blue)}

/* sections */
.sec-head{display:flex;align-items:center;gap:8px;color:var(--pink);font-weight:600;font-size:16px;white-space:nowrap}
.sec-head::after{content:"";flex:1;border-top:2px dotted #ddd;order:1}
.arrows{order:2;display:flex;gap:8px;color:#999;font-size:16px}
.stars{color:var(--star);font-size:14px;letter-spacing:-1px;line-height:1}
.stars b{color:var(--star-off);font-weight:400}
.book h3{font-size:13.5px;font-weight:700;margin-top:14px;line-height:1.3}
.book .author{font-size:12.5px;color:#333;margin:4px 0 6px}
.cover{width:150px;height:225px}
.grid{display:flex}
.featured{top:626px}
.featured .grid{margin-top:22px;padding-left:28px;gap:94px}
.sidebar{position:absolute;left:133px;top:998px;width:215px}
.side-item{display:flex;gap:8px;margin-top:14px}
.side-item .cover{width:85px;height:138px;flex:0 0 85px}
.side-item h3{margin-top:6px;font-size:12.5px}
.side-item .author{font-size:12px}
.old{margin-top:48px}
.btn-blue{display:block;width:204px;height:36px;margin-top:24px;background:linear-gradient(#3aa6ec,#1a80cc);color:#fff;font-weight:700;font-size:14px;text-align:center;line-height:36px;border-radius:3px}
.latest{position:absolute;left:377px;top:998px;width:696px}
.latest .grid{flex-wrap:wrap;gap:0 89px;margin-top:24px;padding-left:25px}
.latest .book{width:150px;height:355px}

/* social band */
.band{position:absolute;top:1746px;left:0;width:1200px;height:318px;background:var(--band)}
.col-head{display:flex;align-items:center;gap:8px;font-size:17px;color:#222;white-space:nowrap}
.col-head::after{content:"";flex:1;border-top:2px dotted #ccc}
.band-col{position:absolute;top:22px}
.band p{font-size:12px;line-height:1.5;color:#333;margin-top:12px}
.band a{color:var(--blue);text-decoration:none}
.field{width:267px;height:32px;background:#dcdcdc;border:1px solid #c4c4c4;margin-top:12px;padding:0 14px;line-height:30px;color:#555;font-size:13px}
.btn-sub{width:126px;height:34px;margin-top:18px;background:linear-gradient(#3aa6ec,#1a80cc);color:#fff;text-align:center;line-height:34px;border-radius:2px;font-size:14px}
.fb-card{display:flex;gap:10px;margin-top:6px;font-size:13px}
.fb-mark{width:64px;height:58px;background:var(--blue);border-radius:4px;flex:0 0 64px}
.fb-card small{display:block;color:#777;font-size:12px;margin-top:3px}
.like{display:inline-block;border:1px solid #aac;background:#eef;font-size:11px;padding:0 6px;margin-top:4px}
.friends{display:grid;grid-template-columns:repeat(4,50px);gap:12px 37px;margin-top:18px}
.friend span{display:block;width:50px;height:50px}
.friend em{display:block;font-style:normal;font-size:10px;color:#666;text-align:center;margin-top:2px}

/* footer */
.footer-cols{position:absolute;top:2105px;left:130px;width:943px;display:flex;gap:22px}
.footer-cols div{width:218px}
.footer-cols ul{list-style:none;margin-top:14px}
.footer-cols li{font-size:12px;color:#333;line-height:23px;white-space:nowrap}
.footer-cols li::before{content:"› "}
.rule{position:absolute;top:2274px;left:130px;width:943px;border-top:2px dotted #ddd}
.copy{position:absolute;top:2294px;left:130px;font-size:11.5px;color:#444}
.cards{position:absolute;top:2282px;right:136px;display:flex;gap:8px}
.cards span{width:56px;height:34px;border:1px solid #bbb;border-radius:3px;background:#f6f6f6;font-size:11px;font-weight:700;color:#1a3e8c;text-align:center;line-height:32px}
</style>
</head>
<body>

<header>
  <div class="wrap brand">
    <span class="brand-mark"></span>
    <span class="brand-name">Online BookStore</span>
    <div class="social"><span>Friendbook</span><span>Chirpline</span><span>Linkroll</span><span>Globeplus</span></div>
  </div>
  <div class="wrap toolbar">
    <div class="search">
      <span class="search-input">Search you book</span>
      <span class="search-by">By</span>
      <span class="search-field">Title <svg width="12" height="34" viewBox="0 0 12 34"><path d="M2 15l4 4 4-4" fill="none" stroke="#333" stroke-width="2"/></svg></span>
      <span class="search-btn">Search</span>
    </div>
    <div class="account"><span>Sign in ▾</span><span>Cart ▾</span><span>Wish list ▾</span></div>
  </div>
  <nav class="nav"><ul>
    <li>NEW RELEASES</li><li>BEST SELLERS</li><li>ART</li><li>HISTORY</li><li>ISSUES &amp; EVENTS</li><li>SCIENCE &amp; NATURE</li><li>CHILDREN'S BOOKS</li><li>E-BOOKS</li><li>SELL YOUR BOOKS</li>
  </ul></nav>
</header>

<div class="hero-band"></div>
<section class="wrap hero">
  <div class="hero-copy">
    <h1>A NUMERICAL TAPESTRY</h1>
    <h2>Patterns &amp; Problem Solving</h2>
    <div class="by">By Arun Devalka</div>
    <p>Some of the favourite problem solving strategies of one of the world's most accomplished Mathematical Olympiad Winners!</p>
  </div>
  <div class="hero-buy"><span class="price">$25.00</span><span class="btn-light">Buy Now!</span></div>
  <div class="hero-cover" role="img" aria-label="Book cover spread of A Numerical Tapestry with author photo and colourful egg artwork"></div>
  <div class="dots"><i></i><i></i><i></i><i></i><i></i></div>
</section>

<section class="wrap featured">
  <div class="sec-head">FEATURED<span class="arrows">‹ ›</span></div>
  <div class="grid">
    <div class="book"><div class="cover" role="img" aria-label="Cover of The Paper Secret: folded paper on autumn leaves" style="background:linear-gradient(#8a3b12,#c2692a 60%,#5a2a10)"></div><h3>The Paper Secret</h3><div class="author">Mira Goldwyn</div><div class="stars">★★★★<b>★</b></div></div>
    <div class="book"><div class="cover" role="img" aria-label="Cover of Buried Streets: city lights and tunnel" style="background:linear-gradient(#4a4440,#8a6a50 45%,#2a2a2a)"></div><h3>Buried Streets</h3><div class="author">Moss Garrow</div><div class="stars">★★★★<b>★</b></div></div>
    <div class="book"><div class="cover" role="img" aria-label="Cover of Lamp of Attention: cream cover with red band" style="background:linear-gradient(#f1e3c0 75%,#b8232a 75%)"></div><h3>Lamp of Attention</h3><div class="author">Navelle</div><div class="stars">★★★★<b>★</b></div></div>
    <div class="book"><div class="cover" role="img" aria-label="Cover of Lights Above Us: old engraving of sky phenomena" style="background:linear-gradient(90deg,#e3b323 14%,#e8e4dc 14%,#b9b3aa)"></div><h3>Lights Above Us</h3><div class="author">Jules Varenne</div><div class="stars">★★★★<b>★</b></div></div>
  </div>
</section>

<aside class="sidebar">
  <div class="sec-head">BEST SELLERS<span class="arrows">‹ ›</span></div>
  <div class="side-item"><div class="cover" role="img" aria-label="Cover of Captured Voices: red poster illustration" style="background:linear-gradient(#d8482a,#a42418)"></div><div class="book"><h3>Captured Voices</h3><div class="author">Noel Chalmsby</div><div class="stars">★★★★<b>★</b></div></div></div>
  <div class="side-item"><div class="cover" role="img" aria-label="Cover of Tiny Engines of Life: molecular sphere on dark blue" style="background:linear-gradient(#1c2e52,#0d1526)"></div><div class="book"><h3>Tiny Engines of Life</h3><div class="author">Jonah Franke</div><div class="stars">★★★★<b>★</b></div></div></div>
  <div class="side-item"><div class="cover" role="img" aria-label="Cover of Asia, Rivers and Beyond: blue abstract" style="background:linear-gradient(#2d8fcf,#7fc2ea)"></div><div class="book"><h3>Asia, Rivers and Beyond</h3><div class="author">Nadia and Weng</div><div class="stars">★★★★<b>★</b></div></div></div>

  <div class="sec-head old">OLD BOOKS<span class="arrows">‹ ›</span></div>
  <div class="side-item"><div class="cover" role="img" aria-label="Cover of Literary Harbourtown: bookshelves photo" style="height:112px;background:linear-gradient(#5a4a3a,#2e2620)"></div><div class="book"><h3>Literary Harbourtown</h3><div class="author">Steven Grimshaw</div><div class="stars">★★★★<b>★</b></div></div></div>
  <span class="btn-blue">Sale Your Old Books</span>
</aside>

<section class="latest">
  <div class="sec-head">LATEST<span class="arrows">‹ ›</span></div>
  <div class="grid">
    <div class="book"><div class="cover" role="img" aria-label="Cover of The Logic of Voting Systems: coloured squares on black" style="background:#242424"></div><h3>The Logic of Voting Systems</h3><div class="author">Paul Mitford</div><div class="stars">★★★★<b>★</b></div></div>
    <div class="book"><div class="cover" role="img" aria-label="Cover of No Regrets: author portrait" style="background:linear-gradient(#e8edf3,#a9b8cc)"></div><h3>No Regrets</h3><div class="author">Matt Rowland</div><div class="stars">★★★★<b>★</b></div></div>
    <div class="book"><div class="cover" role="img" aria-label="Cover of The New Fiddler: green illustrated landscape" style="background:linear-gradient(#3c5a1e,#8fbf3a 60%,#4c7a22)"></div><h3>The New Fiddler</h3><div class="author">Kate Thornfield</div><div class="stars">★★★★<b>★</b></div></div>
    <div class="book"><div class="cover" role="img" aria-label="Cover of Outbreak Hunter: dark red with bird silhouette" style="background:linear-gradient(#b01a1a,#5a0808)"></div><h3>Outbreak Hunter</h3><div class="author">Maureen Mehan Appleby</div><div class="stars">★★★★<b>★</b></div></div>
    <div class="book"><div class="cover" role="img" aria-label="Cover of Four Shillings: orange shirt and tie" style="background:linear-gradient(#f2621c,#d8400c)"></div><h3>Four Shillings</h3><div class="author">Elliot Pearlson</div><div class="stars">★★★★<b>★</b></div></div>
    <div class="book"><div class="cover" role="img" aria-label="Cover of Rail Rider: colourful line lettering on white" style="background:#fafafa;border:3px solid #d4202a"></div><h3>Rail Rider</h3><div class="author">Tarik Gresham</div><div class="stars">★★★★<b>★</b></div></div>
  </div>
</section>

<section class="band">
  <div class="band-col" style="left:140px;width:277px">
    <div class="col-head">Subscribtion</div>
    <p>Lorem ipsum dolor sit amet, consectetur elit, sed do eiusmod tempor incididunt ut labore.</p>
    <div class="field">Name</div>
    <div class="field">Email</div>
    <div class="btn-sub">Subscribe</div>
  </div>
  <div class="band-col" style="left:462px;width:278px">
    <div class="col-head">Chirpline</div>
    <p>Lorem ipsum dolor sit amet, consectetur elit, sed doeius eiusmod tempor incididunt ut labore:<br><a>http://blog.chirpline.com/2013/09/online-book-store-on-chirpline-1.html....</a></p>
    <p>Lorem ipsum dolor sit amet, consectetur elit, sed doeius eiusmod tempor incididunt ut labore:<br><a>http://blog.chirpline.com/2013/09/online-book-store-on-chirpline-1.html....</a></p>
    <p>Lorem ipsum dolor sit amet, consectetur elit, sed doeius eiusmod tempor incididunt ut labore:<br><a>http://blog.chirpline.com/2013/09/online-book-store-on-chirpline-1.html....</a></p>
  </div>
  <div class="band-col" style="left:790px;width:283px">
    <div class="col-head">Friendbook</div>
    <div class="fb-card"><span class="fb-mark"></span><div>Online BookStore on Friendbook<small>12,512,124 people like</small><span class="like">Like</span></div></div>
    <div class="friends">
      <div class="friend"><span role="img" aria-label="Profile photo" style="background:#dfe4ec"></span><em>Konrad</em></div>
      <div class="friend"><span role="img" aria-label="Profile photo" style="background:#8a6a58"></span><em>Anna</em></div>
      <div class="friend"><span role="img" aria-label="Profile photo" style="background:#7a8a9a"></span><em>Dawid</em></div>
      <div class="friend"><span role="img" aria-label="Profile photo" style="background:#3a3a3a"></span><em>Katarzyna</em></div>
      <div class="friend"><span role="img" aria-label="Profile photo" style="background:#9ab8c0"></span><em>Mateusz</em></div>
      <div class="friend"><span role="img" aria-label="Profile photo" style="background:#4a4a52"></span><em>Ariel</em></div>
      <div class="friend"><span role="img" aria-label="Profile photo" style="background:#6a6a6a"></span><em>Marta</em></div>
      <div class="friend"><span role="img" aria-label="Profile photo" style="background:#d8a040"></span><em>Kasia</em></div>
    </div>
  </div>
</section>

<footer>
  <div class="footer-cols">
    <div><div class="col-head">Information</div><ul><li>About Us</li><li>Delivery Information</li><li>Privacy Policy</li><li>Terms &amp; Conditions</li></ul></div>
    <div><div class="col-head">Customer Service</div><ul><li>Contact Us</li><li>Returns</li><li>Site Map</li></ul></div>
    <div><div class="col-head">Extras</div><ul><li>Brands</li><li>Gift Vouchers</li><li>Affiliates</li><li>Specials</li></ul></div>
    <div><div class="col-head">My Account</div><ul><li>My Account</li><li>Order History</li><li>Wish List</li><li>Newsletter</li></ul></div>
  </div>
  <div class="rule"></div>
  <div class="copy">© 2013 Online BookStore. All Right Reserved</div>
  <div class="cards"><span>Vantis</span><span>PayWell</span><span>Amerigo</span><span>Cirrol</span></div>
</footer>

</body>
</html>
```